Wordpress Design Project (Millbrook)

We need a wordpress design for an established auction and real estate company based in California. The winning design will incorporate a creative layout, pleasing color scheme and logo in a very professional and clean manner.

Industry/Entity Type

Real Estate

Requirements
Must have
• Client likes the overall look of http://vornpeq.com/. Site will use the logo colors and maybe complimentary highlight color. Note from client: "“It's important that the appearance of the site will be unique and easily recognizable. In general try to avoid too many colors especially bright and negative contention colors such as bright red, orange, yellow and such. "

The layout should be close as the mentioned reference site except the slideshow (image attached) should be placed below navigation, perhaps at top of content area for the page. Sidebar widgets will include:
- SMS signup form
- Register to bid call to action (as in reference site)
- Email signup form (with only "enter email" field)
- Blog feature "News & Events"
- Social media icons for facebook, twitter, google+, RSS

Navigation:
1) Home
2) Auctions
3) Online Auctions
4) Past Auctions
5) About Us
6) FAQ
7) Blog
8) Contact Us
Nice to have
• Site will have drop-down menus, idea of these would be nice for any of the primary navigation tabs.
Should not have
• please use no auction gavels in the design

```html
<!DOCTYPE html>
<html lang="en">
<head>
<meta charset="utf-8">
<title>Millbrook Auctions</title>
<link rel="stylesheet" href="https://fonts.googleapis.com/css2?family=Arimo:wght@400;700&family=PT+Sans:wght@400;700&display=swap">
<style>
:root{
  --teal:#0f5a51;
  --teal-dark:#083f38;
  --teal-light:#1b7f73;
  --olive:#6d6b3d;
  --page:#e6e6e6;
  --card:#d9d9d9;
  --rose:#c58a8a;
  --slide-border:#a3151a;
  --ink:#1a1a1a;
  --link:#4a48d8;
  --gold:#f5c02a;
  --brown:#4a3218;
  --white:#fff;
}
*{box-sizing:border-box;margin:0;padding:0}
html,body{width:917px;height:1200px;overflow:hidden}
body{position:relative;background:var(--page);font-family:"Arimo",Arial,sans-serif;color:var(--ink);font-size:11px}
.abs{position:absolute}
.topline{left:0;top:0;width:917px;height:4px;background:var(--rose)}
.header{left:0;top:4px;width:917px;height:110px;background:var(--white)}
.brand{left:127px;top:52px;display:flex;align-items:center;gap:6px;font-weight:700;font-size:17px;color:var(--teal)}
.brand-mark{width:14px;height:14px;background:var(--teal)}
.social{top:10px;display:flex;gap:7px;left:666px}
.social span{width:32px;height:32px;border-radius:6px;display:block}
.contact-top{right:115px;text-align:right;color:var(--brown)}
.contact-top.phone{top:68px;font-size:19px}
.contact-top.mail{top:92px;font-size:13px}
.contact-top svg{vertical-align:middle;margin-right:6px}
.nav{left:0;top:114px;width:917px;height:26px;background:var(--teal)}
.nav ul{list-style:none;display:flex;position:absolute;left:115px;top:8px}
.nav li{color:var(--white);font-size:10px;flex:none;white-space:nowrap}
.content-bg{left:104px;top:140px;width:709px;height:870px;background:var(--white)}
.slider{left:104px;top:140px;width:709px;height:242px;border:3px solid var(--slide-border);background:linear-gradient(90deg,#6b4a2e,#b88a4e 30%,#d8b070 55%,#7a3a2a 80%,#a08a70)}
.slider-arrow{top:240px}
.dots{left:432px;top:366px;display:flex;gap:3px}
.dots span{width:11px;height:11px;background:#333;color:#fff;font-size:8px;text-align:center;line-height:11px;border:1px solid #aaa}
.dots span.on{background:#fff;color:#333}
.dropdown{left:164px;top:140px;width:121px;height:63px;background:rgba(15,90,81,.88);padding:3px 8px;font-family:"PT Sans",sans-serif;color:#fff;font-size:10px;line-height:18.5px}
.welcome-title{left:117px;top:394px;font-size:19px;font-weight:400}
.welcome-text{left:117px;top:418px;width:500px;font-size:9.6px;line-height:12.2px;color:#222;letter-spacing:.3px}
.section-title{left:117px;top:504px;font-size:16px;font-weight:400}
.card{left:117px;width:498px;background:var(--card)}
.card-head{height:17px;background:var(--teal);color:#fff;font-size:10px;font-weight:700;padding:3px 13px;letter-spacing:.2px}
.card-sub{position:absolute;left:14px;top:19px;font-size:10px;color:#5a4a10}
.card-photo{position:absolute;left:16px;top:33px;width:137px;height:108px;border:2px solid #777}
.card-body{position:absolute;left:160px;top:31px;width:330px;font-size:10px;line-height:12.6px}
.kind{color:#5a4a10;font-size:10.5px;margin-bottom:2px}
.label{font-weight:700;color:#5a4a10}
.bid{color:var(--link);margin:6px 0 7px}
.bid svg{vertical-align:middle;margin-right:5px}
.details{position:absolute;right:15px;color:var(--link);font-size:10px}
.details svg{vertical-align:middle;margin-right:3px}
.widget{left:633px;width:167px;background:var(--teal);border:3px solid var(--olive);color:#fff}
.widget h3{font-family:"PT Sans",sans-serif;font-weight:400;font-size:15px;padding:6px 0 0 10px;display:flex;align-items:center;gap:4px}
.widget h3 i{width:14px;height:12px;background:#cfe3d8;display:inline-block;border-radius:2px}
.field{position:absolute;left:12px;width:139px;height:21px;background:#eee;color:#555;font-size:8.5px;padding:6px 5px}
.btn{position:absolute;background:var(--gold);border:1px solid #b8860b;border-radius:3px;color:#4a3000;font-weight:700;font-size:9.5px;text-align:center;padding:3px 0}
.news{left:633px;top:712px;width:167px;height:288px;background:var(--teal);border:1px solid var(--teal-light)}
.news h3{height:25px;background:var(--teal-light);font-family:"PT Sans",sans-serif;font-weight:400;font-size:15px;color:#fff;padding:3px 0 0 18px}
.news-item{position:absolute;left:8px;width:150px;font-size:9.5px;line-height:11.5px;color:#fff;padding-left:12px}
.news-item::before{content:"›";position:absolute;left:0;top:-2px;color:var(--gold);font-weight:700;font-size:13px}
.news-item em{display:block;text-align:right;font-style:normal;font-size:7.5px;font-weight:700;color:var(--gold);margin-top:2px}
.footer{left:0;top:1010px;width:917px;height:164px;background:var(--teal);color:#fff}
.footer h4{position:absolute;font-weight:400;font-size:15px;color:#cfd8d4;top:10px}
.footer-rule{position:absolute;top:32px;height:1px;background:#2d7a6f}
.sitemap{position:absolute;left:118px;top:42px;list-style:none;font-size:10px;line-height:14px}
.badge{position:absolute;background:#e8e8e8;border:2px solid #1b1b1b}
.company{position:absolute;left:626px;top:43px;font-size:12px}
.addr{position:absolute;left:626px;width:190px;display:grid;grid-template-columns:46px 1fr;font-size:9px;line-height:11.5px}
.addr dt,.addr dd{margin:0}
.copyright{left:0;top:1174px;width:917px;height:26px;background:var(--teal-dark);color:#cfd8d4;font-size:8px;text-align:center;padding-top:8px}
</style>
</head>
<body>
<div class="abs topline"></div>
<header class="abs header"></header>
<div class="abs brand"><span class="brand-mark"></span>Millbrook Auctions</div>
<div class="abs social" aria-label="Social links">
  <span style="background:#3b5ea8"></span><span style="background:#3aaee0"></span><span style="background:#e8701a"></span><span style="background:#d23c2a"></span>
</div>
<div class="abs contact-top phone"><svg width="12" height="11" viewBox="0 0 12 11"><path d="M1 3C1 1 3 1 6 1s5 0 5 2v1H8V3H4v1H1z M3 5h6l2 5H1z" fill="#333"/></svg>(555) 014-7720</div>
<div class="abs contact-top mail"><svg width="13" height="9" viewBox="0 0 13 9"><rect x=".5" y=".5" width="12" height="8" fill="#f3e3a0" stroke="#b99a3a"/><path d="M.5.5l6 4 6-4" fill="none" stroke="#b99a3a"/></svg>admin@millbrookauctions.com</div>

<nav class="abs nav"><ul>
  <li style="width:69px">HOME</li><li style="width:88px">AUCTIONS</li><li style="width:89px">ABOUT US</li><li style="width:59px">FAQ</li><li style="width:67px">BLOG</li><li>CONTACT US</li>
</ul></nav>

<div class="abs content-bg"></div>
<div class="abs slider" role="img" aria-label="Photo of an antiques shop interior with glassware and furniture"></div>
<svg class="abs slider-arrow" style="left:116px" width="24" height="44" viewBox="0 0 24 44"><path d="M20 2L4 22l16 20" fill="none" stroke="#fff" stroke-width="2"/></svg>
<svg class="abs slider-arrow" style="left:776px" width="24" height="44" viewBox="0 0 24 44"><path d="M4 2l16 20L4 42" fill="none" stroke="#fff" stroke-width="2"/></svg>
<div class="abs dots"><span class="on">1</span><span>2</span><span>3</span><span>4</span></div>
<div class="abs dropdown">- Current Auctions<br>- Past Auctions<br>- Online Auctions</div>

<h1 class="abs welcome-title">Welcome to Millbrook Actions</h1>
<p class="abs welcome-text">Lorem Ipsum. Proin gravida nibh vel velit auctor aliquet. Aenean sollicitudin, lorem quis bibendum auctor, nisi elit consequat ipsum, nec sagittis sem nibh id elit. Duis sed odio sit amet nibh vulputate cursus a sit amet mauris. Morbi accumsan ipsum velit. Nam nec tellus a odio tincidunt auctor a ornare odio. Sed non mauris vitae erat consequat auctor eu in elit. Class aptent taciti sociosqu ad litora torquent per conubia nostra, per inceptos himenaeos. Mauris in erat justo. Nullam ac urna eu felis dapibus condimentum sit amet a augue. Sed</p>

<h2 class="abs section-title">Current Auctions</h2>

<article class="abs card" style="top:528px;height:152px">
  <div class="card-head">END OF JUNE COIN AUCTION</div>
  <div class="card-sub">This will be a night event!</div>
  <div class="card-photo" role="img" aria-label="Photo of coins in plastic holders" style="background:linear-gradient(135deg,#8a9098,#d8dde0 50%,#6a7078)"></div>
  <div class="details" style="top:34px"><svg width="13" height="13"><rect x="1" y="1" width="10" height="11" fill="#dfe8f5" stroke="#4a7ab0"/></svg>Details</div>
  <div class="card-body">
    <div class="kind">LIVE ON-SITE AUCTION</div>
    <div><span class="label">Begins:</span> Monday, march 3rd, 2013 at 4:00 PM</div>
    <div class="bid"><svg width="16" height="8"><rect width="16" height="8" rx="2" fill="#7aa0c8"/></svg>Click Here to Bid Online Now!</div>
    <div><span class="label">Location:</span> Lorem ipsum, DD 6688</div>
    <p style="margin-top:5px">Lorem Ipsum. Proin gravida nibh vel velit auctor aliquet. Aenean sollicitudi, lorem quis bibendum auctor, nisi elit consequat ipsum, nec sagittis sem</p>
    <p style="margin-top:5px;margin-left:-4px">This Auction is live with online bidding!</p>
  </div>
</article>

<article class="abs card" style="top:688px;height:152px">
  <div class="card-head">ESTATE AUCTION-REAL ESTATE AND PERSONAL PROPERTY</div>
  <div class="card-sub">Lorem ipsum proin gravida</div>
  <div class="card-photo" role="img" aria-label="Photo of a two-storey house with garage" style="background:linear-gradient(180deg,#c9d6e0,#a8a090 50%,#5f7a45)"></div>
  <div class="details" style="top:34px"><svg width="13" height="13"><rect x="1" y="1" width="10" height="11" fill="#dfe8f5" stroke="#4a7ab0"/></svg>Details</div>
  <div class="details" style="top:53px"><svg width="13" height="11"><rect x="1" y="2" width="11" height="8" fill="#f3d060" stroke="#a07a10"/></svg>Photo Galleries</div>
  <div class="card-body">
    <div class="kind">LIVE ON-SITE AUCTION WITH ONLINE BIDDING</div>
    <div><span class="label">Begins:</span> Wednesday, May 29, 2013 at 10:00 AM</div>
    <div class="bid"><svg width="16" height="8"><rect width="16" height="8" rx="2" fill="#7aa0c8"/></svg>Click Here to Bid Online Now!</div>
    <div><span class="label">Location:</span> Lorem ipsum, DD 6688</div>
    <p style="margin-top:5px">Lorem Ipsum. Proin gravida nibh vel velit auctor aliquet. Aenean sollicitudin, lorem quis bibendum auctor, nisi elit consequat ipsum, nec sagittis sem nibh id elit. Duis sed odio sit amet nibh vulputate cursus a sit</p>
  </div>
</article>

<article class="abs card" style="top:849px;height:151px">
  <div class="card-head">APRIL CWP CLASS</div>
  <div class="card-sub">Saturday, May 31th</div>
  <div class="card-photo" role="img" aria-label="Photo of assorted consumer electronics" style="background:linear-gradient(135deg,#e8eef2,#505860 45%,#c0302a 70%,#f0f0f0)"></div>
  <div class="details" style="top:34px"><svg width="13" height="13"><rect x="1" y="1" width="10" height="11" fill="#dfe8f5" stroke="#4a7ab0"/></svg>Details</div>
  <div class="card-body" style="top:45px">
    <div><span class="label">Location:</span> Lorem ipsum, DD 6688</div>
    <p style="margin-top:5px">Lorem Ipsum. Proin gravida nibh vel velit auctor aliquet. Aenean sollicitudin, lorem quis bibendum auctor, nisi elit consequat ipsum, nec sagittis sem nibh id elit. Duis sed odio sit amet nibh vulputate cursus a sit amet mauris. Morbi accumsan ipsum velit. Nam nec tellus a odio tincidunt auctor a ornare odio. Sed non mauris vitae erat consequat auctor eu in elit. Class aptent taciti</p>
  </div>
</article>

<aside class="abs widget" style="top:398px;height:185px">
  <h3><i></i>SMS Signup form</h3>
  <div style="position:absolute;left:12px;top:33px;font-size:9.5px;font-weight:700;line-height:13px">I wish to:<br>
    <span style="display:inline-block;width:7px;height:7px;border-radius:50%;background:#ccc"></span> Subscribe &nbsp;<span style="display:inline-block;width:7px;height:7px;border-radius:50%;background:#ccc"></span> Unsubscribe</div>
  <div class="field" style="top:67px">Enter Your Name:</div>
  <div class="field" style="top:97px">Enter Your Cell phone #:</div>
  <div class="field" style="top:127px;width:119px">Select Service provider :</div>
  <svg style="position:absolute;left:131px;top:127px" width="20" height="21"><rect width="20" height="21" fill="#2a8aa0"/><path d="M5 8l5 5 5-5" fill="none" stroke="#fff" stroke-width="2"/></svg>
  <div class="btn" style="left:84px;top:157px;width:67px">Confirm</div>
</aside>

<aside class="abs widget" style="top:596px;height:104px">
  <h3><i></i>Sign up Newsletter</h3>
  <div class="field" style="top:33px">Enter Your Email Address..</div>
  <div class="btn" style="left:84px;top:63px;width:67px">Subscribe</div>
</aside>

<aside class="abs news">
  <h3>News &amp; Events</h3>
  <div class="news-item" style="top:32px">Lorem Ipsum. Proin gravida mj nibh vel velit auctor aliquet op.<em>View details</em></div>
  <div class="news-item" style="top:89px">Lorem Ipsum. Proin gravida mj nibh vel velit auctor aliquet op.<em>View details</em></div>
  <div class="news-item" style="top:143px">Lorem Ipsum. Proin gravida mj nibh vel velit auctor aliquet op.<em>View details</em></div>
  <div class="news-item" style="top:201px">Lorem Ipsum. Proin gravida mj nibh vel velit auctor aliquet op.<em>View details</em></div>
  <div class="news-item" style="top:245px">Lorem Ipsum. Proin gravida mj nibh vel velit auctor aliquet op.<em>View details</em></div>
</aside>

<footer class="abs footer">
  <h4 style="left:117px">Sitemap</h4>
  <div class="footer-rule" style="left:117px;width:460px"></div>
  <ul class="sitemap"><li>Home</li><li>Auctions</li><li>About Us</li><li>FAQ</li><li>Blog</li><li>Contact Us</li></ul>
  <div class="badge" style="left:340px;top:50px;width:86px;height:36px;border-radius:3px"></div>
  <div class="badge" style="left:446px;top:44px;width:76px;height:40px;border-radius:50%"></div>
  <div class="badge" style="left:334px;top:98px;width:38px;height:46px"></div>
  <div class="badge" style="left:380px;top:98px;width:30px;height:46px"></div>
  <div class="badge" style="left:420px;top:106px;width:100px;height:30px"></div>
  <h4 style="left:626px">Contact Info</h4>
  <div class="footer-rule" style="left:626px;width:174px"></div>
  <div class="company">Millbrook Actions</div>
  <dl class="addr" style="top:60px">
    <dt>Address:</dt><dd style="font-size:8.6px">Lorem Ipsum. Proin gravida nibh vel velit auctor aliquet. Aenean sollicitu-</dd>
  </dl>
  <dl class="addr" style="top:90px;line-height:14.5px">
    <dt>Tel:</dt><dd>(555) 014 7731</dd>
    <dt>Fax:</dt><dd>(555) 014 7732</dd>
    <dt>Email:</dt><dd>info@millbrookauctions.com</dd>
  </dl>
</footer>
<div class="abs copyright">(c) 2013. Millbrook Actions. All Rights Reserved.</div>
</body>
</html>
```